Monastery website with e-commerce

We need a new website more elegant and modern with also a shop for the coffee we produce.
It must appear serious, professional and also beautiful and full of images.
This is our site now: www.casafiorentaria.it

```html
<!DOCTYPE html>
<html lang="en">
<head>
<meta charset="utf-8">
<title>Casa Fiorentaria</title>
<link href="https://fonts.googleapis.com/css2?family=Gloock&family=Plus+Jakarta+Sans:wght@400;500;600;700&display=swap" rel="stylesheet">
<style>
:root{
  --green:#4a6b2e;
  --navy:#153f63;
  --navy-dark:#163a5c;
  --ink:#111;
  --text:#555;
  --muted:#777;
  --light:#f2f2f2;
  --white:#fff;
  --line:#e2e2e2;
  --heading:"Gloock",serif;
  --body:"Plus Jakarta Sans",sans-serif;
}
*{box-sizing:border-box;margin:0;padding:0}
html,body{width:1200px;height:4310px;overflow:hidden}
body{position:relative;font-family:var(--body);color:var(--ink);background:var(--white)}
.abs{position:absolute}
.photo{position:absolute}
h1,h2{font-family:var(--heading);font-weight:400;text-transform:uppercase;line-height:1.45}
.btn{position:absolute;display:flex;align-items:center;justify-content:center;gap:8px;background:var(--green);color:var(--white);border-radius:30px;font-size:14px;font-weight:600;text-transform:uppercase}
.btn svg{width:14px;height:14px}
/* header */
.site-header{position:absolute;left:0;top:0;width:1200px;height:81px;background:var(--white)}
.brand{position:absolute;left:145px;top:14px;display:flex;align-items:center;gap:12px;font-family:var(--body);font-size:22px;font-weight:500;color:#3a2a1a}
.brand-mark{width:52px;height:52px;border-radius:50%;background:#9c1c1c}
.nav{position:absolute;top:24px;height:33px;font-size:14px;font-weight:500;display:flex;align-items:center}
.nav.active{background:var(--navy-dark);color:var(--white);padding:0 11px;left:484px;width:104px;justify-content:center;border-radius:2px}
.cart{position:absolute;left:1020px;top:26px}
/* hero */
.hero{position:absolute;left:0;top:81px;width:1200px;height:544px;background:linear-gradient(180deg,#8ba4b8 0%,#9aa39a 25%,#6f6a55 45%,#4f6b2c 65%,#5a7a2a 85%,#6f8e36 100%)}
.hero h1{position:absolute;left:0;width:1200px;top:122px;text-align:center;color:var(--white);font-size:64px;line-height:1.2}
.hero .sub{position:absolute;width:1200px;top:222px;text-align:center;color:var(--white);font-size:19px}
.hero .cta{position:absolute;left:509px;top:284px;width:182px;height:46px;border:2px solid var(--white);border-radius:30px;background:var(--green);color:var(--white);display:flex;align-items:center;justify-content:center;gap:10px;font-size:15px;font-weight:600}
.scroll{position:absolute;width:1200px;top:486px;text-align:center;color:var(--white);font-size:11px}
/* courses */
.courses h2{position:absolute;width:1200px;top:688px;text-align:center;font-size:35px}
.courses .lead{position:absolute;width:1200px;top:758px;text-align:center;font-size:13px;color:var(--text)}
.courses .link{position:absolute;width:1200px;top:799px;text-align:center;font-size:17px;color:var(--navy)}
.card{position:absolute;background:var(--white);box-shadow:0 6px 20px rgba(0,0,0,.1);text-align:center;font-size:16px;line-height:1.6;color:#222}
.card .photo{left:0;top:0;width:100%}
.card p{position:absolute;left:0;width:100%;bottom:20px}
.arrow{position:absolute;width:38px;height:38px;border-radius:50%;display:flex;align-items:center;justify-content:center}
/* christians */
.about-band{position:absolute;left:0;top:1306px;width:1200px;height:621px;background:var(--light)}
.box{position:absolute;background:var(--white);box-shadow:0 4px 16px rgba(0,0,0,.08)}
.box::after{content:"";position:absolute;inset:8px;border:1px solid var(--line)}
.box h2{position:absolute;font-size:36px;line-height:52px}
.box .copy{position:absolute;font-size:13px;line-height:24px;color:var(--muted)}
/* visit */
.visit{position:absolute;left:0;top:1927px;width:1200px;height:403px;background:linear-gradient(180deg,#3a3f44 0%,#5a4d3a 40%,#6b4a24 65%,#3b4a2a 100%)}
.visit h2{position:absolute;width:1200px;top:60px;text-align:center;color:var(--white);font-size:36px;line-height:53px}
.visit .copy{position:absolute;left:130px;width:940px;top:182px;text-align:center;color:var(--white);font-size:13px;line-height:25px}
.visit .call{position:absolute;width:1200px;top:251px;text-align:center;color:var(--white);font-size:17px}
.phone-btn{position:absolute;left:514px;top:294px;width:172px;height:44px;border:2px solid var(--white);border-radius:30px;background:var(--green);color:var(--white);display:flex;align-items:center;gap:14px;padding-left:6px;font-size:15px;font-weight:600}
.phone-btn .dot{width:32px;height:32px;border-radius:50%;background:var(--white);display:flex;align-items:center;justify-content:center}
/* product */
.product h2{position:absolute;left:646px;top:2440px;font-size:36px}
.product .copy{position:absolute;left:647px;top:2506px;width:420px;font-size:13px;line-height:24px;color:var(--muted)}
.ticks{position:absolute;left:647px;top:2586px;list-style:none;font-size:11px;color:var(--muted)}
.ticks li{display:flex;align-items:center;gap:7px;height:26px}
/* place */
.place{position:absolute;left:0;top:3406px;width:1200px;height:402px;background:var(--navy)}
.place h2{position:absolute;width:1200px;top:56px;text-align:center;color:var(--white);font-size:35px;line-height:52px}
.place .addr{position:absolute;width:1200px;top:183px;text-align:center;color:var(--white);font-size:17px}
/* footer */
.foot-nav{position:absolute;top:4036px;width:1200px;display:flex;justify-content:center;gap:18px;font-size:14px;font-weight:500;color:#222}
.foot-nav span.sep{color:#222}
.contact{position:absolute;top:4114px;display:flex;gap:14px;align-items:flex-start}
.contact .ic{width:28px;height:28px;border-radius:50%;background:var(--green);display:flex;align-items:center;justify-content:center;margin-top:3px}
.contact b{display:block;font-weight:500;font-size:14px;color:#222}
.contact small{font-size:12px;color:var(--muted)}
.vline{position:absolute;top:4114px;width:1px;height:40px;background:var(--line)}
.hline{position:absolute;left:144px;top:4177px;width:911px;height:1px;background:var(--line)}
.legal{position:absolute;width:1200px;top:4206px;text-align:center;font-size:12px;color:var(--text)}
.social{position:absolute;width:26px;height:26px;border-radius:50%;background:#e4e4e4;top:4247px}
.social.on{background:var(--navy)}
</style>
</head>
<body>

<header class="site-header">
  <div class="brand"><span class="brand-mark"></span>Casa Fiorentaria</div>
  <div class="nav active">Who We Are</div>
  <div class="nav" style="left:623px">Hesychasm</div>
  <div class="nav" style="left:748px">Courses</div>
  <div class="nav" style="left:849px">Coffee</div>
  <div class="nav" style="left:942px">Shop</div>
  <svg class="cart" width="30" height="28" viewBox="0 0 30 28" fill="none" stroke="#333" stroke-width="2"><path d="M1 3h4l3 15h15l3-10H7"/><circle cx="10" cy="23" r="2"/><circle cx="21" cy="23" r="2"/><circle cx="27" cy="4" r="4" fill="#4a6b2e" stroke="none"/></svg>
</header>

<section class="hero" role="img" aria-label="Alpine mountain peaks above a green forested valley">
  <h1>Welcome to Serenity</h1>
  <p class="sub">Let's Save Humans and Animals!</p>
  <div class="cta">GET STARTED <svg width="16" height="14" viewBox="0 0 16 14" fill="none" stroke="#fff" stroke-width="2"><path d="M1 7h13M9 2l5 5-5 5"/></svg></div>
  <p class="scroll">Scroll Down<br>⌄</p>
</section>

<section class="courses">
  <h2>We are naturopaths and spagyrists</h2>
  <p class="lead">Check out our two-year Naturopathy course and the online courses in Meditation, Self-Healing, Spagyric Medicine and many others</p>
  <p class="link">Discover Our Upcoming Online Courses</p>

  <div class="arrow" style="left:105px;top:1049px;background:#fff;box-shadow:0 2px 8px rgba(0,0,0,.15)"><svg width="12" height="12" viewBox="0 0 12 12" fill="none" stroke="#222" stroke-width="2"><path d="M8 1L3 6l5 5"/></svg></div>
  <div class="arrow" style="left:1057px;top:1049px;background:var(--green)"><svg width="12" height="12" viewBox="0 0 12 12" fill="none" stroke="#fff" stroke-width="2"><path d="M4 1l5 5-5 5"/></svg></div>

  <div class="card" style="left:169px;top:907px;width:288px;height:315px">
    <div class="photo" style="height:226px;background:linear-gradient(135deg,#c9a58e,#4f5f66)" role="img" aria-label="Cupped hands holding carved numerology stones"></div>
    <p>Online Numerology Course,<br>From February 6, 2025</p>
  </div>
  <div class="card" style="left:745px;top:907px;width:288px;height:315px">
    <div class="photo" style="height:226px;background:linear-gradient(135deg,#5a4a32,#8a7a4a)" role="img" aria-label="Mortar and pestle among bowls of dried herbs"></div>
    <p>Online Herbalism Course, From<br>February 13, 2025</p>
  </div>
  <div class="card" style="left:457px;top:850px;width:288px;height:320px;z-index:2">
    <div class="photo" style="height:229px;background:linear-gradient(135deg,#2e241c,#7a5a3a)" role="img" aria-label="Monk preparing spagyric remedies in a workshop"></div>
    <p>Spagyric Medicine Course<br>From February 13, 2025</p>
  </div>
</section>

<section class="about-band">
  <div class="photo" style="left:144px;top:70px;width:521px;height:474px;background:linear-gradient(135deg,#b8a576,#5a6a3a)" role="img" aria-label="Monk seated beside a white goat in a meadow"></div>
  <div class="box" style="left:490px;top:70px;width:565px;height:348px">
    <h2 style="left:38px;top:38px">We are Christians<br>of the East</h2>
    <p class="copy" style="left:40px;top:152px;width:490px">We are a community of monks and lay people who seek God through the Gospel, meditation and contemplation Yeshua and through daily work.<br>We save people and animals.</p>
    <div class="btn" style="left:40px;top:260px;width:173px;height:41px">Find out more <svg viewBox="0 0 14 14" fill="none" stroke="#fff" stroke-width="2"><path d="M1 7h11M8 3l4 4-4 4"/></svg></div>
  </div>
</section>

<section class="visit" role="img" aria-label="Autumn forest under a stormy sky">
  <h2>What is important to know before<br>coming to visit us</h2>
  <p class="copy">We are open to the public on Sundays, from 9am to 12pm and from 2:30pm to 5pm. At 11 we celebrate the Divine Liturgy. We are still a work in progress so you will have to be patient. You can taste our coffee, visit the restored parts and talk to us.</p>
  <p class="call">For Visits on Other Days Call Us Now:</p>
  <div class="phone-btn"><span class="dot"><svg width="16" height="16" viewBox="0 0 16 16" fill="none" stroke="#4a6b2e" stroke-width="1.6"><path d="M4 2l2 3-1.5 1.5a8 8 0 0 0 5 5L11 10l3 2-1 2.5C7 14 2 9 1.5 3z"/></svg></span>055-0149382</div>
</section>

<section class="product">
  <div class="photo" style="left:144px;top:2409px;width:427px;height:358px;background:linear-gradient(135deg,#6a9a3a,#8a6a44 55%,#2f5a20)" role="img" aria-label="Burlap sack full of roasted coffee beans among leaves"></div>
  <h2>Our Product</h2>
  <p class="copy">Lorem ipsum dolor sit amet, consectetur adipiscing elit, sed do eiusmod tempor incididunt ut labore et dolore magna aliqua.<br>Ut enim ad minim veniam, quis nostrud exercitation</p>
  <ul class="ticks">
    <li><svg width="11" height="11" viewBox="0 0 12 12"><circle cx="6" cy="6" r="6" fill="#153f63"/><path d="M3 6l2 2 4-4" stroke="#fff" stroke-width="1.6" fill="none"/></svg>Duis aute irure dolor in reprehenderit</li>
    <li><svg width="11" height="11" viewBox="0 0 12 12"><circle cx="6" cy="6" r="6" fill="#153f63"/><path d="M3 6l2 2 4-4" stroke="#fff" stroke-width="1.6" fill="none"/></svg>Excepteur sint occaecat cupidatat non proident</li>
    <li><svg width="11" height="11" viewBox="0 0 12 12"><circle cx="6" cy="6" r="6" fill="#153f63"/><path d="M3 6l2 2 4-4" stroke="#fff" stroke-width="1.6" fill="none"/></svg>Sed ut perspiciatis unde omnis iste natus error</li>
  </ul>
  <div class="btn" style="left:648px;top:2689px;width:132px;height:41px">Buy now <svg viewBox="0 0 14 14" fill="none" stroke="#fff" stroke-width="2"><path d="M1 7h11M8 3l4 4-4 4"/></svg></div>

  <div class="photo" style="left:536px;top:2852px;width:519px;height:474px;background:linear-gradient(135deg,#3a2a1e,#6a4a30 50%,#1a1a1a)" role="img" aria-label="Hands holding freshly roasted coffee beans"></div>
  <div class="box" style="left:144px;top:2856px;width:566px;height:344px">
    <h2 style="left:38px;top:34px">We are roasters of a<br>supreme coffee</h2>
    <p class="copy" style="left:40px;top:152px;width:460px">We produce rare quality wood-roasted coffee with ancient blends. Coffee produced and sent to your home and above all with a roasting with an intense and real flavor.</p>
    <div class="btn" style="left:40px;top:256px;width:236px;height:42px">Discover our coffees <svg viewBox="0 0 14 14" fill="none" stroke="#fff" stroke-width="2"><path d="M1 7h11M8 3l4 4-4 4"/></svg></div>
  </div>
</section>

<section class="place">
  <h2>We are in a wonderful place<br>come and visit us!</h2>
  <p class="addr">Casa Fiorentaria, Valdorsa Hills Via Collina Alta 12 - 50099 Valdorsa (FI)</p>
</section>
<div class="photo" style="left:144px;top:3654px;width:440px;height:305px;background:linear-gradient(180deg,#3a6a9a,#4a5a2a 40%,#c9a040 80%)" role="img" aria-label="Yellow monastery building beneath a large cedar tree"></div>
<div class="photo" style="left:614px;top:3654px;width:441px;height:305px;background:linear-gradient(180deg,#b8c0b0,#6a8a3a 45%,#d8d4cc 80%)" role="img" aria-label="Child feeding a herd of white goats in a field"></div>

<nav class="foot-nav">
  <span>WHO WE ARE</span><span class="sep">I</span><span>HESYCHASM</span><span class="sep">I</span><span>COURSES</span><span class="sep">I</span><span>COFFEE</span><span class="sep">I</span><span>SHOP</span>
</nav>

<div class="contact" style="left:144px"><span class="ic"><svg width="14" height="14" viewBox="0 0 16 16" fill="#fff"><path d="M4 1l2.5 3.5L5 6.5a8 8 0 0 0 4.5 4.5L11.5 9.5 15 12l-1 3C6 15 1 10 1 2z"/></svg></span><div><b>Phone</b><small>055 0149382</small></div></div>
<div class="vline" style="left:345px"></div>
<div class="contact" style="left:418px"><span class="ic"><svg width="12" height="14" viewBox="0 0 12 16" fill="#fff"><path d="M6 0a6 6 0 0 0-6 6c0 4.5 6 10 6 10s6-5.5 6-10a6 6 0 0 0-6-6zm0 8.5A2.5 2.5 0 1 1 6 3.5a2.5 2.5 0 0 1 0 5z"/></svg></span><div><b>Location</b><small>Via Collina Alta 12 50099 Valdorsa</small></div></div>
<div class="vline" style="left:775px"></div>
<div class="contact" style="left:841px"><span class="ic"><svg width="14" height="10" viewBox="0 0 14 10" fill="#fff"><rect width="14" height="10" rx="1"/><path d="M1 1l6 4.5L13 1" stroke="#4a6b2e" stroke-width="1.4" fill="none"/></svg></span><div><b>E-mail</b><small>info@casafiorentaria.it</small></div></div>
<div class="hline"></div>

<p class="legal">© 2025 Casa Fiorentaria - All Rights Reserved &nbsp; I &nbsp; Privacy Policy &nbsp; I &nbsp; Terms &amp; Conditions &nbsp; I &nbsp; Cookie Policy</p>
<span class="social" style="left:536px"></span>
<span class="social" style="left:571px"></span>
<span class="social on" style="left:605px"></span>
<span class="social" style="left:638px"></span>

</body>
</html>
```